Mark & Lisa's Hammock Season Party

Invitation to a party 60-80 people at a private residence. Age range 30-40s.

Themes: summer/casual/Australian backyard/local community

**For delivery via both email and printed copy**
Would like one document suitable for both purposes or two versions for electronic or paper invitation. I will arrange printing so please prepare it in a suitable format.

Specimen text attached. Address and phone contact to follow by message with successful bidder

Thanks!
Mark

Target Market(s)

Locals, friends. Party attendees will typicaly be parents in their forties who who be leaving the kids at home for a relaxed party night, and walking home afterward

Industry/Entity Type

Community

Font styles to use
Sans Serif

Requirements
Should not have
• Cliche Australiana imagery. No kangaroos etc

```html
<!DOCTYPE html>
<html lang="en">
<head>
<meta charset="utf-8">
<title>Mark &amp; Lisa's Hammock Season Party</title>
<link rel="stylesheet" href="https://fonts.googleapis.com/css2?family=Bebas+Neue&family=Yellowtail&family=Abril+Fatface&family=Mulish:wght@400;600;700;800&display=swap">
<style>
  :root {
    --red: #e0141b;
    --red-dark: #a80f14;
    --ink: #3a3a3a;
    --paper: #ffffff;
    --glow: #fbe3e3;
  }
  * { box-sizing: border-box; margin: 0; padding: 0; }
  html, body { width: 836px; height: 1200px; overflow: hidden; background: var(--paper); }
  .invite {
    position: relative;
    width: 836px;
    height: 1200px;
    background: var(--paper);
    font-family: "Mulish", sans-serif;
    color: var(--ink);
  }
  .string-lights {
    position: absolute;
    left: 0; top: 98px;
    width: 836px; height: 222px;
    background: linear-gradient(180deg, var(--glow) 0%, #fff3f3 60%, var(--paper) 100%);
  }
  .ribbon {
    position: absolute;
    left: 0; top: 52px;
    width: 836px; height: 100px;
  }
  .ribbon-text {
    position: absolute;
    top: 75px;
    font-family: "Bebas Neue", sans-serif;
    font-size: 33px;
    line-height: 44px;
    color: var(--paper);
    letter-spacing: 0.3px;
    white-space: nowrap;
  }
  .ribbon-text.left { left: 139px; }
  .ribbon-text.right { left: 448px; }
  .ribbon-amp {
    position: absolute;
    left: 399px; top: 64px;
    width: 50px;
    text-align: center;
    font-family: "Yellowtail", cursive;
    font-size: 50px;
    line-height: 60px;
    color: var(--paper);
  }
  .title {
    position: absolute;
    left: 0; top: 330px;
    width: 836px;
    text-align: center;
    font-family: "Yellowtail", cursive;
    font-weight: 400;
    font-size: 84px;
    line-height: 84px;
    color: var(--red);
  }
  .title span { display: block; }
  .audience {
    position: absolute;
    left: 0; top: 540px;
    width: 836px;
    text-align: center;
    font-size: 33px;
    font-weight: 400;
    color: var(--red);
  }
  .ruled {
    position: absolute;
    left: 82px;
    width: 672px;
    display: flex;
    align-items: center;
    gap: 16px;
    color: var(--red);
    font-weight: 800;
  }
  .ruled::before, .ruled::after {
    content: "";
    flex: 1;
    height: 3px;
    background: var(--red);
  }
  .ruled.day { top: 594px; font-size: 31px; }
  .ruled.time { top: 723px; font-size: 31px; }
  .date {
    position: absolute;
    left: 0; top: 622px;
    width: 836px;
    text-align: center;
    font-family: "Abril Fatface", serif;
    font-size: 86px;
    line-height: 100px;
    letter-spacing: 5px;
    color: var(--ink);
  }
  .address {
    position: absolute;
    left: 0; top: 772px;
    width: 836px;
    text-align: center;
    font-family: "Bebas Neue", sans-serif;
    font-size: 49px;
    line-height: 52px;
    color: var(--red);
  }
  .details {
    position: absolute;
    left: 83px; top: 860px;
    width: 672px; height: 266px;
    border: 5px dotted var(--red);
  }
  .details-tag {
    position: absolute;
    left: 300px; top: 843px;
    width: 236px; height: 36px;
  }
  .details-tag-label {
    position: absolute;
    left: 300px; top: 843px;
    width: 236px;
    text-align: center;
    font-size: 19px;
    font-weight: 700;
    line-height: 36px;
    color: var(--paper);
  }
  .details-list {
    position: absolute;
    left: 90px; top: 895px;
    width: 656px;
    list-style: none;
    text-align: center;
    font-size: 18.5px;
    font-weight: 600;
    line-height: 23px;
    color: var(--ink);
  }
  .details-list li { margin-bottom: 12px; }
</style>
</head>
<body>
<main class="invite">
  <div class="string-lights" role="img" aria-label="Festoon string of red party lights hanging across the top of the invitation"></div>

  <svg class="ribbon" viewBox="0 52 836 100" width="836" height="100" aria-hidden="true">
    <polygon points="112,84 124,98 112,112 128,112 128,84" fill="var(--red-dark)"/>
    <polygon points="724,84 712,98 724,112 708,112 708,84" fill="var(--red-dark)"/>
    <polygon points="114,73 722,73 708,97 722,121 114,121 128,97" fill="var(--red)"/>
    <rect x="128" y="112" width="580" height="10" fill="var(--ink)"/>
    <polygon points="114,73 722,73 708,97 722,121 114,121 128,97" fill="var(--red)"/>
    <polygon points="423,46 433,54 446,50 452,62 465,64 466,77 477,84 472,96 480,106 470,114 472,127 459,130 454,142 441,140 432,150 423,142 414,150 405,140 392,142 387,130 374,127 376,114 366,106 374,96 369,84 380,77 381,64 394,62 400,50 413,54" fill="var(--ink)" transform="translate(0,6)"/>
    <polygon points="423,46 433,54 446,50 452,62 465,64 466,77 477,84 472,96 480,106 470,114 472,127 459,130 454,142 441,140 432,150 423,142 414,150 405,140 392,142 387,130 374,127 376,114 366,106 374,96 369,84 380,77 381,64 394,62 400,50 413,54" fill="var(--red)"/>
  </svg>
  <span class="ribbon-text left">Leave the kids at home</span>
  <span class="ribbon-amp">&amp;</span>
  <span class="ribbon-text right">Let your hair down at</span>

  <h1 class="title">
    <span>Mark &amp; Lisa's</span>
    <span>Hammock Season Party</span>
  </h1>

  <p class="audience">For Corella Rise and friends</p>

  <p class="ruled day">Saturday</p>
  <p class="date">02.01.2016</p>
  <p class="ruled time">From 6pm 'til late</p>

  <p class="address">25 Abcdefg Street, Corella Rise</p>

  <section class="details">
  </section>
  <svg class="details-tag" viewBox="0 0 236 36" width="236" height="36" aria-hidden="true">
    <polygon points="0,0 236,0 222,18 236,36 0,36 14,18" fill="var(--red)"/>
  </svg>
  <span class="details-tag-label">Child-free event</span>
  <ul class="details-list">
    <li>Dress: summer casual, bare feet welcome</li>
    <li>Cocktail food provided</li>
    <li>BYO but only if you insist</li>
    <li>If you have some friends or neighbours that you like<br>to hang out with, we would love to meet. Bring them with you!</li>
    <li>An RSVP for catering would be nice.<br>Text Mark xxx xxxxxx or Lisa yyyyyyyy before Xmas please.</li>
  </ul>
</main>
</body>
</html>
```